Flyer-Design für Grosshandelsunternehmen für Papeterie- und Bürobedarf
Zielgruppe
KOLDIG ist ein Schweizer Grosshandelsunternehmen für Papeterie- und Bürobedarf. Kunden sind ausschliesslich professionelle Wiederverkäufer. Endverbraucher werden nicht direkt, sondern über KOLDIG Kunden beliefert.
Das Sortiment umfasst neben Papeterie- und Schulartikeln eine kompetente Auswahl im Bereich Bürobedarf. Die Produktepalette wird laufend weiterentwickelt und umfasst auch den Bereich Catering & Kaffee, Hygiene & Reinigung sowie Betriebssicherheit – alles was im modernen Büro benötigt wird.
KOLDIG bietet seinen Kunden umfassende Dienstleistungen an. Diese ermöglichen es, das vom Markt geforderte breite und tiefe Sortiment zielgruppengerecht erfolgreich zu vermarkten und effizient zu verteilen. In enger Zusammenarbeit mit unseren Kunden und Lieferanten entwickeln wir unsere Dienstleistungen stetig weiter. Neben den Vermarktungszielen stehen Effizienzziele, die Doppelspurigkeiten in der Wertschöpfungskette vermeiden, im Vordergrund.
Das oberste Ziel von KOLDIG ist es, ein zuverlässiger Partner zu sein. Deshalb geniessen Servicegrad und Lieferqualität höchste Priorität. Wir streben nach kooperativen und langfristigen Geschäftsbeziehungen und setzen neue Technologien zum gemeinsamen Nutzen ein.
Aufgabenstellung
Erstellung eines 8-seitigen Layoutes, welches als Einleitung eines 600-seitigen Kataloges erscheint. Gemäss Briefing Vorlage, Dateiname Briefing_Trend_entwurfshalle.pdf. Texte können zu 100% übernommen werden und sollen in das von Ihnen vorgeschlagene Layout einfliessen, keine Änderungen vornehmen , nicht kürzen. Ihre Aufgabe besteht darin zum Text ein passendes Layout oder passende Grafiken zu erstellen. Wichtig; Die Bilder im Briefing sind als Anregung unsere Bildwelt Katalog gedacht, bitte integrieren Sie neue Bilder, welche zu Ihrem vorgeschlagenen Layout passen.
- InDesign Dokument
- Format 230 x 297 mm inkl. 3 mm Beschnitt
- Doppelseiten-Layout
- Anzahl Seiten 8
- Sprache deutsch
- Schrift vom Musterlayout übernehmen (ClanOT Schriftfamilie) keine anderen Schriften benützen, wichtig
- Grafische Elemente, wir benötigen am Ende die Originaldateien

```html
<!DOCTYPE html>
<html lang="de">
<head>
<meta charset="utf-8">
<title>Workplace Trend – Katalogeinleitung</title>
<link href="https://fonts.googleapis.com/css2?family=Encode+Sans+Condensed:wght@300;400;600;800&display=swap" rel="stylesheet">
<style>
:root{
  --bg:#cfcfcf;
  --paper:#ffffff;
  --teal:#4dbfb3;
  --teal-faint:#d3efec;
  --grey-label:#8c8c8e;
  --text:#555a5e;
  --head:#3d4245;
  --tape:#b9bcbd;
}
*{box-sizing:border-box;margin:0;padding:0}
html,body{width:1200px;height:3613px;overflow:hidden;background:var(--bg)}
body{position:relative;font-family:"Encode Sans Condensed",sans-serif;color:var(--text)}
.page{position:absolute;background:var(--paper);overflow:hidden}
.band-top{position:absolute;left:0;right:0;top:0;height:8px;background:var(--teal)}
.band-bottom{position:absolute;left:0;right:0;bottom:0;height:8px;background:var(--teal)}
.photo{position:absolute}
.num{position:absolute;font-weight:800;font-size:96px;line-height:1;color:var(--teal-faint);letter-spacing:-2px}
.head{position:absolute;text-align:right}
.head-top{font-weight:300;font-size:27px;line-height:1;color:var(--head);letter-spacing:1px}
.head-main{font-weight:800;font-size:42px;line-height:1;color:var(--teal);border-bottom:2px solid var(--teal);padding-bottom:2px;letter-spacing:.5px}
.copy{position:absolute;font-weight:300;font-size:8.6px;line-height:1.55;color:var(--text)}
.copy p{margin-bottom:9px}
.copy b{font-weight:600;color:var(--head)}
.label{position:absolute;height:22px;line-height:22px;padding:0 10px;font-weight:600;font-size:13px;color:#fff;letter-spacing:.5px;white-space:nowrap}
.label.grey{background:var(--grey-label)}
.label.teal{background:var(--teal)}
.badge{position:absolute;width:100px;height:100px;background:var(--teal);color:#fff;text-align:center;transform:rotate(-3deg);padding-top:12px;box-shadow:0 1px 3px rgba(0,0,0,.15)}
.badge::before,.badge::after{content:"";position:absolute;width:30px;height:12px;background:var(--tape);opacity:.85}
.badge::before{top:-3px;right:-10px;transform:rotate(45deg)}
.badge::after{bottom:-3px;left:-10px;transform:rotate(45deg)}
.badge .b-small{font-weight:300;font-size:11px;line-height:1.05;letter-spacing:.5px}
.badge .b-big{font-weight:800;font-size:16px;line-height:1;margin:4px 6px;padding:3px 0;border-top:1px solid #fff;border-bottom:1px solid #fff;letter-spacing:.5px}
.section-title{position:absolute;font-weight:800;font-size:40px;color:var(--teal);line-height:1;border-bottom:2px solid var(--teal);padding-bottom:2px;letter-spacing:.5px}
.stat{position:absolute;font-weight:300;font-size:8.4px;line-height:1.5;width:140px}
.ring{position:absolute}
</style>
</head>
<body>

<!-- Seite 1 -->
<section class="page" style="left:391px;top:93px;width:428px;height:602px">
  <div class="photo" role="img" aria-label="Foto: Menschen gehen eilig durch einen Bürogang mit Holzwand" style="left:0;top:0;width:214px;height:230px;background:linear-gradient(160deg,#b9a58d,#8a7a6a 60%,#5d6a7a)"></div>
  <div class="photo" role="img" aria-label="Foto: Kollegen mit Gesichtsmaske begrüssen sich mit dem Ellbogen" style="left:0;top:237px;width:214px;height:233px;background:linear-gradient(150deg,#d8d6d3,#8f8e8e 60%,#4d4f53)"></div>
  <div class="head" style="left:217px;top:18px;width:211px;text-align:center">
    <div class="head-top">WORKPLACE</div>
    <div class="head-main" style="padding-bottom:4px">TREND</div>
  </div>
  <div class="photo" role="img" aria-label="Foto: zwei Mitarbeitende schauen lachend auf ein Tablet" style="left:223px;top:110px;width:205px;height:328px;background:linear-gradient(140deg,#e6e3dc,#b58e6e 45%,#6b5646)"></div>
  <div class="badge" style="left:270px;top:372px"><div class="b-small">FÜR SIE<br>HABEN WIR DIE</div><div class="b-big">KOMPETENZ</div><div class="b-small">IN ALLEN<br>BEREICHEN</div></div>
  <div class="num" style="left:4px;top:510px;font-size:88px">01</div>
  <div class="copy" style="left:22px;top:492px;width:384px">
    <p>Als Experte für Büro-Bedarf und Büroausstattung bieten wir Ihnen ein umfassendes Produkt­sortiment für jeden Anwendungsbereich.</p>
    <p>Unsere Produkte unterstützen Sie bei der Einhaltung von Hygienekonzepten in den unterschied­lichen Arbeitsbereichen, wobei wir unsere Schwerpunkte genauso auf die Datensicherheit Ihres Unternehmens oder die Ausstattung von Arbeitsplätzen legen.</p>
  </div>
  <div class="band-bottom"></div>
</section>

<!-- Seiten 2–3 -->
<section class="page" style="left:157px;top:758px;width:887px;height:627px">
  <div class="band-top"></div>
  <div class="label grey" style="left:0;top:43px">VERHINDERUNG VON</div>
  <div class="label teal" style="left:0;top:73px">AUSBRÜCHEN</div>
  <div class="num" style="left:322px;top:22px">02</div>
  <div class="photo" role="img" aria-label="Grafik: Menschen mit Abstand auf einem weissen Netz aus Verbindungslinien" style="left:0;top:110px;width:443px;height:250px;background:radial-gradient(ellipse at 50% 60%,#ffffff,#e3f1f5 60%,#c9dde4)"></div>
  <div class="badge" style="left:308px;top:292px"><div class="b-small">FÜR SIE<br>HABEN WIR DIE</div><div class="b-big">KOMPETENZ</div><div class="b-small">IN ALLEN<br>BEREICHEN</div></div>
  <div class="section-title" style="left:22px;top:376px;padding-right:12px;width:278px">EINLEITUNG</div>
  <div class="copy" style="left:22px;top:436px;width:400px">
    <p>Covid-19 beeinflusst aktuell, und mit hoher Wahrscheinlichkeit auch noch längere Zeit, Unternehmen aller Branchen. Unabhängig davon, ob es sich um einen Produktionsbetrieb, Büros, Ladengeschäfte oder Home-Office handelt.</p>
    <p>In jedem Bereich entstehen in dieser Situation neue Bedürfnisse, für die wir als kompetenter Partner die richtige Lösung liefern. Unsere Produkte unterstützen Sie effizient und wirksam im Bereich Social Distancing und realisieren Hygiene-Konzepte entsprechend der Vorgaben.</p>
    <p>Speziell für den Infektionsschutz entwickelte Produkte schützen Mitarbeiter am Arbeitsplatz und Ihre Kunden.</p>
  </div>

  <div class="head" style="left:560px;top:40px;width:190px">
    <div class="head-top">BÜRO UND</div>
    <div class="head-main">BETRIEB</div>
  </div>
  <div class="num" style="left:775px;top:22px">03</div>
  <div class="copy" style="left:467px;top:135px;width:400px">
    <p>Die regelmässige Desinfektion der Hände und des Arbeitsplatzes ist eine wirksame Massnahme, um das Infektionsrisiko nachweislich zu minimieren. Dies gilt vor allem für Büros mit Mobile Desk oder Desksharing. Hier ist die gründliche Oberflächenreinigung im Rahmen des Infektionsschutzes unverzichtbar. Aber auch nur von einer Person genutzte Schreibtische erfordern zuverlässige Hygiene. Unsere speziell für die Oberflächenreinigung entwickelten Desinfektions- und Reinigungsmittel stellen die Einhaltung der Vorgaben zum Infektionsschutz sicher.</p>
    <p>Ergänzend zu den desinfizierenden Massnahmen bilden optisch attraktive Trennwände zusätzlichen Schutz, während Hinweisschilder in Meeting-Räumen die Besprechungs-Teilnehmer an die Vorgaben des Hygienekonzepts erinnern.</p>
    <p>Für den Empfangsbereich führen wir ein umfangreiches Produktsortiment von der Desinfektion, über Leitsysteme bis zu gut verständlichen Piktogrammen.</p>
  </div>
  <div class="photo" role="img" aria-label="Foto: Frau mit Maske desinfiziert einen Schreibtisch" style="left:443px;top:331px;width:267px;height:288px;background:linear-gradient(150deg,#dfe3e6,#9aa3a9 50%,#3e3f43)"></div>
  <div class="photo" role="img" aria-label="Foto: Mitarbeitende mit Maske im Büro" style="left:716px;top:331px;width:171px;height:288px;background:linear-gradient(150deg,#e4e6e8,#a6a39a 50%,#c8973a)"></div>
  <div class="badge" style="left:650px;top:330px"><div class="b-small">FÜR SIE<br>HABEN WIR DIE</div><div class="b-big">KOMPETENZ</div><div class="b-small">IN ALLEN<br>BEREICHEN</div></div>
  <div class="band-bottom"></div>
</section>

<!-- Seiten 4–5 -->
<section class="page" style="left:157px;top:1444px;width:887px;height:627px">
  <div class="band-top"></div>
  <div class="head" style="left:130px;top:33px;width:190px">
    <div class="head-top">BETRIEBS</div>
    <div class="head-main">BEDARF</div>
  </div>
  <div class="num" style="left:330px;top:22px">04</div>
  <div class="copy" style="left:22px;top:128px;width:400px">
    <p>Mit der Reinigung mit speziell auf das Hygienekonzept abgestimmten Reinigungsmitteln minimieren Sie die Virenbelastung von Oberflächen in allen Unternehmensbereichen und unterwegs auf Geschäfts­reise. Für zusätzliche Sicherheit sorgt ein ausreichend grosser Abstand zu anderen Personen.</p>
    <p>Diesen erreichen Sie im Hotel, in der Gastro oder auf Messen durch Bodenmarkierungen und durch­dachte Leitsysteme. Schilder, Kleber und Tafeln bieten Platz für richtige Hinweise und unterstützen die installierten Leitsysteme durch Zusatzinformationen.</p>
    <p>Absperrbänder verhindern das Betreten gesperrter Bereiche und Trennwände sorgen auf Messen, im Hotel und im Gastro-Bereich für Diskretion und zusätzlichen Schutz.</p>
  </div>
  <div class="label grey" style="left:343px;top:276px">AUFKLEBER</div>
  <div class="label teal" style="left:322px;top:306px">SCHILDER UND</div>
  <div class="label grey" style="left:368px;top:336px">TAFELN</div>
  <div class="photo" role="img" aria-label="Foto: Abstandsmarkierungen mit Fussspuren auf dem Boden und Absperrpfosten" style="left:0;top:289px;width:246px;height:330px;background:linear-gradient(160deg,#f4f6f8,#c6ccd6 55%,#454d72)"></div>
  <div class="photo" role="img" aria-label="Foto: Bodenaufkleber mit Hinweis auf 1,5 m Abstand" style="left:254px;top:289px;width:189px;height:330px;background:linear-gradient(150deg,#8d8f91,#d9d9d9 45%,#f2f2f2 70%,#9c9e9f)"></div>
  <div class="badge" style="left:25px;top:480px"><div class="b-small">FÜR SIE<br>HABEN WIR DIE</div><div class="b-big">KOMPETENZ</div><div class="b-small">IN ALLEN<br>BEREICHEN</div></div>

  <div class="head" style="left:560px;top:33px;width:190px;text-align:center">
    <div class="head-top">WASCH</div>
    <div class="head-main" style="text-align:center">RAUM</div>
  </div>
  <div class="num" style="left:775px;top:22px">05</div>
  <div class="copy" style="left:467px;top:128px;width:400px">
    <p>Mit unserem umfangreichen Produktsortiment unterstützen wir Sie, die Hygienemassnahmen in Wa­schräumen auf hohem Niveau umzusetzen.</p>
    <p>Speziell für die Oberflächendesinfektion entwickelte Produkte sorgen für bakterien- und keimfreie Sanitäranlagen, während schonende Reinigungsmittel die allgemeine Sauberkeit im Waschraum gewährleisten. Ein weiteres Thema ist das professionelle Waste-Management für die korrekte Ent­sorgung des vorhandenen Abfalls.</p>
    <p>Hier bilden geschlossene Abfalleimer eine wichtige Voraussetzung, um eine Belastung des Umfeldes mit Keimen und Viren zu minimieren.</p>
    <p>Denn wirksamer Infektionsschutz am Arbeitsplatz betrifft alle von Ihren Mitarbeitern genutzten Räume im Unternehmen.</p>
  </div>
  <div class="label grey" style="left:462px;top:325px;width:425px;font-size:13.5px">DIE QUALITÄT DER TOILETTEN AM ARBEITSPLATZ IST</div>
  <div class="photo" role="img" aria-label="Foto: moderner Waschraum mit Waschbecken und Spiegel" style="left:670px;top:350px;width:217px;height:269px;background:linear-gradient(160deg,#eef0f1,#a9b1b7 50%,#3a3d41)"></div>
  <div class="label teal" style="left:462px;top:360px">BESONDERS WICHTIG!</div>
  <div class="stat" style="left:467px;top:414px">Eine ordentliche und gepflegte Toilette am Arbeitsplatz zeugt von Fürsorge für die Mitarbeiter.</div>
  <div class="stat" style="left:467px;top:484px">Eine saubere Toilette verbessert das Gefühl des Wohlbefindens bei der Arbeit.</div>
  <div class="stat" style="left:467px;top:556px">Verfügbarkeit von Toilettenpapier ist ein Muss.</div>
  <svg class="ring" style="left:610px;top:406px" width="60" height="200" viewBox="0 0 60 200" aria-hidden="true">
    <g fill="#fff" stroke-width="4">
      <circle cx="30" cy="30" r="26" stroke="#e3e6e7"/><circle cx="30" cy="30" r="26" stroke="#4dbfb3" stroke-dasharray="132 164" transform="rotate(-90 30 30)"/>
      <circle cx="30" cy="98" r="26" stroke="#e3e6e7"/><circle cx="30" cy="98" r="26" stroke="#4dbfb3" stroke-dasharray="131 164" transform="rotate(-90 30 98)"/>
      <circle cx="30" cy="166" r="26" stroke="#e3e6e7"/><circle cx="30" cy="166" r="26" stroke="#4dbfb3" stroke-dasharray="149 164" transform="rotate(-90 30 166)"/>
    </g>
    <g fill="#4dbfb3" font-family="Encode Sans Condensed, sans-serif" font-weight="800" font-size="13" text-anchor="middle">
      <text x="30" y="35">81%</text><text x="30" y="103">80%</text><text x="30" y="171">91%</text>
    </g>
  </svg>
  <div class="badge" style="left:757px;top:352px"><div class="b-small">FÜR SIE<br>HABEN WIR DIE</div><div class="b-big">KOMPETENZ</div><div class="b-small">IN ALLEN<br>BEREICHEN</div></div>
  <div class="band-bottom"></div>
</section>

<!-- Seiten 6–7 -->
<section class="page" style="left:157px;top:2137px;width:887px;height:626px">
  <div class="band-top"></div>
  <div class="head" style="left:130px;top:33px;width:190px;text-align:center">
    <div class="head-top">DATEN</div>
    <div class="head-main" style="text-align:center">SCHUTZ</div>
  </div>
  <div class="num" style="left:330px;top:22px">06</div>
  <div class="copy" style="left:22px;top:128px;width:400px">
    <p>Trotz eindeutiger gesetzlicher Vorgaben und einheitlicher Datenschutzstandards gehen viele Mit­arbeiter im Unternehmen noch nachlässig mit sensiblen Daten um.</p>
    <p>Die Folgen für das Unternehmen können gravierend sein und ziehen im Ernstfall hohe Strafen nach sich. Während der Zugriff auf digitale Daten aufgrund durchdachter Sicherheitsmassnahmen für unbefugte Personen immer schwieriger wird, gelangen auf Papier gedruckte Daten durch den nachlässigen Umgang immer noch viel zu häufig in unbefugte Hände.</p>
    <p>Die Lösung sind spezielle Aktenvernichter, die Daten auf Papier so vernichten, dass je nach Sicher­heitsstufe eine Wiederherstellung unmöglich ist.</p>
    <p>Wir führen Aktenvernichter für unterschiedliche Sicherheitsstufen, die sensible Informationen zuverlässig vernichten. Mit leistungsfähigen Aktenvernichtern lässt sich das <b>Datenleck Papierkorb</b> vermeiden und sensible Daten können absolut sicher vor dem Zugriff Unbefugter entsorgt werden.</p>
    <p>Das Sicherheitsrisiko besteht genauso im privaten Umfeld, im Home-Office, sowie auch in Klein­unternehmen.</p>
  </div>
  <div class="label grey" style="left:100px;top:385px">MINIMIERTES</div>
  <div class="label teal" style="left:78px;top:413px">SICHERHEITSRISIKO</div>
  <div class="photo" role="img" aria-label="Grafik: leuchtendes Schloss-Symbol für Datensicherheit" style="left:0;top:440px;width:140px;height:179px;background:radial-gradient(circle at 45% 45%,#d7eef0,#7fb8c2 50%,#3e6f7c)"></div>
  <div class="photo" role="img" aria-label="Foto: Stapel Papierdokumente mit Hand und Stift" style="left:148px;top:440px;width:295px;height:179px;background:linear-gradient(160deg,#f4f4f4,#c9cacb 55%,#2f3033)"></div>
  <div class="badge" style="left:300px;top:373px"><div class="b-small">FÜR SIE<br>HABEN WIR DIE</div><div class="b-big">KOMPETENZ</div><div class="b-small">IN ALLEN<br>BEREICHEN</div></div>

  <div class="head" style="left:560px;top:33px;width:190px;text-align:center">
    <div class="head-top">HOME</div>
    <div class="head-main" style="text-align:center">OFFICE</div>
  </div>
  <div class="num" style="left:775px;top:22px">07</div>
  <div class="copy" style="left:467px;top:128px;width:400px">
    <p>Seit Beginn der Pandemie gingen viele Mitarbeiter in das Home-Office, und erledigen ihre Arbeit von Zuhause aus.</p>
    <p>Obwohl mittlerweile ein Teil der Arbeitnehmer wieder zurück im Büro ist, entwickelte sich das Home-Office für andere aus einer vorerst temporären zur dauerhaften Lösung.</p>
    <p>Wie im Büro ist jedoch auch bei der Arbeit von zuhause aus die Ergonomie des Arbeitsplatzes und seine professionelle Ausstattung vom PC bis zur <b>Peripherie-Hardware für Print</b> ein wichtiges Thema. In unserem umfangreichen Sortiment für Büroausstattung führen wir eine grosse Auswahl <b>hochwertiger Produkte</b> vom Büro-Stuhl über Bodenschutzmatten bis zu Tastatur und Maus. Ein Headset ist die Voraussetzung, um an einer Video Conference oder einem Webinar teilzunehmen.</p>
  </div>
  <div class="label grey" style="left:462px;top:304px">HOME-OFFICE AUSSTATTUNG</div>
  <div class="photo" role="img" aria-label="Foto: Laptop mit Videokonferenz auf einem Schreibtisch" style="left:462px;top:330px;width:243px;height:289px;background:linear-gradient(150deg,#cfb594,#8b6a4c 50%,#3e4552)"></div>
  <div class="photo" role="img" aria-label="Foto: Frau arbeitet zuhause am Laptop" style="left:713px;top:300px;width:174px;height:319px;background:linear-gradient(150deg,#f4f1ec,#d9c4a8 50%,#c68c2c)"></div>
  <div class="badge" style="left:645px;top:485px"><div class="b-small">FÜR SIE<br>HABEN WIR DIE</div><div class="b-big">KOMPETENZ</div><div class="b-small">IN ALLEN<br>BEREICHEN</div></div>
  <div class="band-bottom"></div>
</section>

<!-- Seite 8 -->
<section class="page" style="left:391px;top:2833px;width:439px;height:619px">
  <div class="band-top"></div>
  <div class="head" style="left:115px;top:33px;width:200px;text-align:center">
    <div class="head-top">NEUES KAPITEL</div>
    <div class="head-main" style="text-align:center">SCHULE</div>
  </div>
  <div class="num" style="left:324px;top:22px">08</div>
  <div class="copy" style="left:22px;top:128px;width:395px">
    <p>Wir haben unser bereits umfangreiches Produktsortiment an Schulbedarf mit den erforderlichen Unterrichtsmaterialien und Hilfsmitteln dem Lehrplan 21 angepasst.</p>
    <p>Dabei liegt der Schwerpunkt auf Unterrichtsmaterialien, die vor allem im kreativen Bereich ein­gesetzt werden. Hochwertige Farbstifte, Acryl-, Öl- und Aquarellfarben zählen dazu. Aber auch Kleister, Klebeband, Leim oder Gips sind ein Teil der Kreativmaterialien.</p>
    <p>Für den Zeichenunterricht benötigte Pinsel, Papier und Tusche finden Sie im Sortiment genauso wie Modellierer-Utensilien wie Spachtel, Schwamm sowie Modellier- und Schnittwerkzeug.</p>
    <p><b>Lehrplan 21:</b> Der Lehrplan legt fest, was Schülerinnen und Schüler in jedem Fachbereich und in jedem Zyklus lernen. Er ist eine Grundlage für die Entwicklung der Lehrmittel, ein Planungs­instrument für Lehrpersonen sowie für die Aus- und Weiterbildung der Lehrpersonen.</p>
  </div>
  <div class="photo" role="img" aria-label="Foto: Kinderhand schreibt Buchstaben in ein Heft" style="left:0;top:326px;width:173px;height:285px;background:linear-gradient(150deg,#e9c9b8,#d49a86 50%,#f1e6df)"></div>
  <div class="photo" role="img" aria-label="Foto: Schüler zeichnet mit Farbstiften am Tisch mit Lehrerin" style="left:180px;top:326px;width:259px;height:285px;background:linear-gradient(150deg,#e8d4b3,#b58a5a 50%,#4a3a30)"></div>
  <div class="badge" style="left:117px;top:322px"><div class="b-small">FÜR SIE<br>HABEN WIR DIE</div><div class="b-big">KOMPETENZ</div><div class="b-small">IN ALLEN<br>BEREICHEN</div></div>
  <div class="band-bottom"></div>
</section>

</body>
</html>
```